依頼詳細
シンプルというよりは、見やすくスッキリとしたデザインで目にとまるようなデザインにしたいです。

・角2封筒 表フルカラー
縦向き、郵便番号枠不要、住所記入線不要

・長3封筒 表フルカラー
横向き、郵便番号枠不要、住所記入線をお願いします。

インクモールへ印刷発注の為、専用テンプレートを使用し、そのままインクモールで印刷依頼が可能な仕様のデータで納品をお願いします。
デザインの印刷範囲制限がありますので、範囲内でお願いします。

封筒の色ですが、インクモールで封筒のサンプルを取り寄せ確認したところ、
クリニックのロゴが木のため、ペールノビア、ミルドトーンリーフがいいのではと考えております。
記載項目
記載項目などは添付ファイルをご参照ください。
希望イメージ
シンプル 複雑
単色 カラフル
暗い 明るい
日常 高級
遊び心 厳粛
未来的 伝統的
女性的 男性的
希望する色
納品ファイル
• 高解像度JPG (.jpg)
• イラストレーター形式 (.ai)
補足説明
添付したロゴを使用してください。
■ 選んだ理由

とてもきれいなデザインで気に入りました。

■ 提案者全員のお礼・コメント

素敵なデザインが多く迷いました。
たくさんのご提案ありがとうございます。

```html
<!DOCTYPE html>
<html lang="ja">
<head>
<meta charset="utf-8">
<title>長3封筒 仕上がりイメージ</title>
<link rel="stylesheet" href="https://fonts.googleapis.com/css2?family=Noto+Sans+JP:wght@400;700&display=swap">
<style>
  :root {
    --page: #ffffff;
    --ink: #222222;
    --outline: #8a8a8a;
    --rule: #9a9a9a;
    --envelope-white: #ffffff;
    --envelope-tint: #b9c3d9;
    --flap-white: #ffffff;
    --flap-tint: #b3bdd4;
    --brand: #2f8a3c;
    --mark: #4aa04f;
  }
  * { margin: 0; padding: 0; box-sizing: border-box; }
  html, body { width: 846px; height: 1200px; overflow: hidden; background: var(--page); }
  body { position: relative; font-family: "Noto Sans JP", sans-serif; color: var(--ink); }
  .sheet-label { position: absolute; left: 42px; font-size: 15px; letter-spacing: 0.02em; }
  .envelope { position: absolute; left: 42px; width: 768px; height: 403px; }
  .envelope svg { position: absolute; inset: 0; }
  .sender { position: absolute; left: 330px; display: flex; align-items: center; gap: 22px; }
  .brand { display: flex; align-items: center; gap: 7px; }
  .brand-dot { width: 26px; height: 26px; border-radius: 50%; background: var(--mark); }
  .brand-text { display: flex; flex-direction: column; line-height: 1.15; }
  .brand-area { font-size: 7px; }
  .brand-name { font-size: 17px; font-weight: 700; color: var(--brand); letter-spacing: 0.04em; }
  .brand-en { font-size: 7px; }
  .contact { font-size: 9.5px; line-height: 1.5; }
</style>
</head>
<body>

  <p class="sheet-label" style="top:132px">■ 長３封筒 ペールノビア仕上がりイメージ</p>
  <div class="envelope" style="top:175px">
    <svg width="768" height="403" viewBox="0 0 768 403">
      <rect x="0.5" y="0.5" width="767" height="402" fill="var(--envelope-white)" stroke="var(--outline)"/>
      <polygon points="0.5,0.5 66,22 66,381 0.5,402.5" fill="var(--flap-white)" stroke="var(--outline)"/>
      <line x1="274" y1="93" x2="691" y2="93" stroke="var(--rule)"/>
      <line x1="274" y1="169" x2="691" y2="169" stroke="var(--rule)"/>
    </svg>
    <div class="sender" style="top:254px">
      <div class="brand">
        <span class="brand-dot"></span>
        <div class="brand-text">
          <span class="brand-area">大阪梅田</span>
          <span class="brand-name">あおば眼科</span>
          <span class="brand-en">Aoba Eye Clinic</span>
        </div>
      </div>
      <div class="contact">
        〒530-0099 大阪市北区梅田9-8-7<br>
        TEL 06-6000-1234<br>
        https://www.aoba-eye.example.jp/
      </div>
    </div>
  </div>

  <p class="sheet-label" style="top:682px">■ 長３封筒 ミルドトーンリーフ仕上がりイメージ</p>
  <div class="envelope" style="top:725px">
    <svg width="768" height="403" viewBox="0 0 768 403">
      <rect x="0.5" y="0.5" width="767" height="402" fill="var(--envelope-tint)" stroke="var(--outline)"/>
      <polygon points="0.5,0.5 66,22 66,381 0.5,402.5" fill="var(--flap-tint)" stroke="var(--outline)"/>
      <line x1="274" y1="87" x2="691" y2="87" stroke="var(--rule)"/>
      <line x1="274" y1="163" x2="691" y2="163" stroke="var(--rule)"/>
    </svg>
    <div class="sender" style="top:254px">
      <div class="brand">
        <span class="brand-dot"></span>
        <div class="brand-text">
          <span class="brand-area">大阪梅田</span>
          <span class="brand-name">あおば眼科</span>
          <span class="brand-en">Aoba Eye Clinic</span>
        </div>
      </div>
      <div class="contact">
        〒530-0099 大阪市北区梅田9-8-7<br>
        TEL 06-6000-1234<br>
        https://www.aoba-eye.example.jp/
      </div>
    </div>
  </div>

</body>
</html>
```